Velvet Basin Suites, a portable luxury restroom trailer company needs a landing page

We need a landing page for a luxury portable restroom trailer company. This should be modern, and simple - use any combination of Pantone colors: Warm Gray 1C, Black 7C, 7529c, 873C, 8003C

We rent these trailers for special events like weddings, private parties, festivals, family reunions, team building, wine tastings, beer tastings, food truck round-ups, etc.

An idea of the landing page is in the files below. Please use stock photography and placeholder text for now. The winning design will be given final content.

Requirements
Must have
• Multiple "Get Quote" buttons or a place for them to type in type of rental, how many people etc

```html
<!DOCTYPE html>
<html lang="en">
<head>
<meta charset="utf-8">
<title>Velvet Basin Suites — Luxury Portable Restroom Trailers</title>
<link href="https://fonts.googleapis.com/css2?family=Roboto+Condensed:wght@400&family=Work+Sans:wght@400;600&family=Mulish:wght@400&display=swap" rel="stylesheet">
<style>
:root{
  --bg:#000000;
  --gold:#e5b53d;
  --panel:#1f1f1f;
  --panel-text:#8e8e8e;
  --white:#ffffff;
  --footer:#1f1f1f;
  --rule:#333333;
}
*{margin:0;padding:0;box-sizing:border-box}
html,body{width:1200px;height:2576px;overflow:hidden;background:var(--bg);color:var(--white)}
body{position:relative;font-family:"Mulish",sans-serif}
.abs{position:absolute}
.heading{font-family:"Roboto Condensed",sans-serif;font-weight:400;color:var(--gold)}

/* header */
.brand{left:162px;top:66px;display:flex;align-items:center;gap:10px;font-size:19px;color:var(--gold);letter-spacing:.5px;white-space:nowrap}
.brand-dot{width:14px;height:14px;border-radius:50%;background:var(--gold);flex:none}
.nav{left:495px;top:70px;display:flex;gap:38px;font-size:15px}
.nav a{color:var(--white);text-decoration:none}
.nav a.active{color:var(--gold)}
.nav-phone{left:892px;top:66px;display:flex;align-items:center;gap:10px;color:var(--gold);font-size:17px}

/* placeholders */
.ph{position:absolute;background:var(--panel);color:var(--panel-text);display:flex;align-items:center;justify-content:center;text-align:center;font-family:"Roboto Condensed",sans-serif;font-size:18px;line-height:22px;overflow:hidden}
.ph.large span{transform:rotate(-45deg);font-size:44px;white-space:nowrap}

.hero-title{left:164px;top:236px;font-size:34px;line-height:47px;width:280px}

/* events */
.events-title{left:590px;top:663px;font-size:32px;line-height:42px}
.event-list{left:590px;top:750px;list-style:none;font-family:"Work Sans",sans-serif;font-size:18px;line-height:27.6px}
.event-list li{display:flex;align-items:center;gap:10px}
.event-list svg{width:9px;height:10px}

.cta{position:absolute;width:321px;height:58px;border:1px solid var(--gold);display:flex;align-items:center;gap:12px;padding-left:12px;color:var(--gold);font-family:"Work Sans",sans-serif;font-weight:600;font-size:16.5px;text-decoration:none;white-space:nowrap}
.quote-btn{position:absolute;width:118px;height:58px;background:var(--gold);color:var(--bg);display:flex;align-items:center;justify-content:center;font-family:"Work Sans",sans-serif;font-weight:600;font-size:16.5px;text-decoration:none;white-space:nowrap}

.products-title{left:0;width:1200px;top:1178px;text-align:center;font-size:40px}
.product-name{font-size:24px}
.product-copy{font-size:13.6px;line-height:21.6px;width:392px}

/* footer */
.footer{left:0;top:2296px;width:1200px;height:280px;background:var(--footer)}
.footer-brand{left:162px;top:2370px;display:flex;align-items:center;gap:12px;font-size:26px;color:var(--gold);white-space:nowrap}
.footer-brand .brand-dot{width:22px;height:22px}
.contact-box{width:46px;height:46px;border:1px solid #bdbdbd;display:flex;align-items:center;justify-content:center}
.contact-label{font-size:17px}
.contact-value{font-size:14px;white-space:nowrap}
.rule{left:162px;top:2477px;width:878px;height:1px;background:var(--rule)}
.copyright{left:0;width:1200px;top:2510px;text-align:center;font-size:14px}
</style>
</head>
<body>

<header>
  <div class="abs brand"><span class="brand-dot"></span>Velvet Basin Suites</div>
  <nav class="abs nav">
    <a class="active" href="#">Home</a>
    <a href="#">Events</a>
    <a href="#">Our Products</a>
    <a href="#">Contact Us</a>
  </nav>
  <div class="abs nav-phone">
    <svg width="24" height="24" viewBox="0 0 24 24" fill="none" stroke="currentColor" stroke-width="1.4"><path d="M5 3l4 1 1 5-2.5 1.5a12 12 0 0 0 6 6L15 14l5 1 1 4-2 2C10 21 3 14 3 5z"/><path d="M14 3a7 7 0 0 1 7 7M14 6a4 4 0 0 1 4 4"/></svg>
    07 5812 6640
  </div>
</header>

<section class="hero">
  <h1 class="abs heading hero-title">We Are Luxury Portable Restroom Trailer Supply Company</h1>
  <div class="ph" role="img" aria-label="Trailer interior photo" style="left:578px;top:172px;width:139px;height:75px">Image Here</div>
  <div class="ph" role="img" aria-label="Event photo" style="left:729px;top:131px;width:112px;height:117px">Image<br>Here</div>
  <div class="ph" role="img" aria-label="Event photo" style="left:854px;top:195px;width:113px;height:116px">Image<br>Here</div>
  <div class="ph" role="img" aria-label="Trailer exterior photo" style="left:463px;top:260px;width:186px;height:115px">Image Here</div>
  <div class="ph" role="img" aria-label="Luxury restroom photo" style="left:658px;top:259px;width:186px;height:180px">Image Here</div>
  <div class="ph" role="img" aria-label="Wedding venue photo" style="left:852px;top:324px;width:186px;height:115px">Image Here</div>
  <div class="ph" role="img" aria-label="Vanity detail photo" style="left:536px;top:387px;width:112px;height:117px">Image<br>Here</div>
  <div class="ph" role="img" aria-label="Festival photo" style="left:661px;top:451px;width:113px;height:117px">Image Here</div>
  <div class="ph" role="img" aria-label="Trailer steps photo" style="left:787px;top:452px;width:139px;height:75px">Image Here</div>
</section>

<section class="events">
  <div class="ph large" role="img" aria-label="Restroom trailer at an event" style="left:161px;top:641px;width:398px;height:468px"><span>Image Here</span></div>
  <h2 class="abs heading events-title">We Rent These Trailers For<br>Special Events</h2>
  <ul class="abs event-list">
    <li><svg viewBox="0 0 9 10" fill="none" stroke="#fff" stroke-width="1.8"><path d="M2 1l4 4-4 4"/></svg>Weddings</li>
    <li><svg viewBox="0 0 9 10" fill="none" stroke="#fff" stroke-width="1.8"><path d="M2 1l4 4-4 4"/></svg>Private Parties</li>
    <li><svg viewBox="0 0 9 10" fill="none" stroke="#fff" stroke-width="1.8"><path d="M2 1l4 4-4 4"/></svg>Festivals</li>
    <li><svg viewBox="0 0 9 10" fill="none" stroke="#fff" stroke-width="1.8"><path d="M2 1l4 4-4 4"/></svg>Family Reunions</li>
    <li><svg viewBox="0 0 9 10" fill="none" stroke="#fff" stroke-width="1.8"><path d="M2 1l4 4-4 4"/></svg>Team Building</li>
    <li><svg viewBox="0 0 9 10" fill="none" stroke="#fff" stroke-width="1.8"><path d="M2 1l4 4-4 4"/></svg>Wine Tastings</li>
    <li><svg viewBox="0 0 9 10" fill="none" stroke="#fff" stroke-width="1.8"><path d="M2 1l4 4-4 4"/></svg>Beer Tastings</li>
    <li><svg viewBox="0 0 9 10" fill="none" stroke="#fff" stroke-width="1.8"><path d="M2 1l4 4-4 4"/></svg>Food Truck</li>
    <li><svg viewBox="0 0 9 10" fill="none" stroke="#fff" stroke-width="1.8"><path d="M2 1l4 4-4 4"/></svg>Round-ups</li>
  </ul>
  <a class="cta" href="#" style="left:590px;top:1019px">
    <svg width="26" height="26" viewBox="0 0 24 24" fill="none" stroke="currentColor" stroke-width="1.4"><path d="M5 3l4 1 1 5-2.5 1.5a12 12 0 0 0 6 6L15 14l5 1 1 4-2 2C10 21 3 14 3 5z"/><path d="M14 3a7 7 0 0 1 7 7M14 6a4 4 0 0 1 4 4"/></svg>
    Contact Us Today 555.018.2247
  </a>
  <a class="quote-btn" href="#" style="left:922px;top:1019px">Get Quote</a>
</section>

<section class="products">
  <h2 class="abs heading products-title">Our Products</h2>

  <h3 class="abs heading product-name" style="left:160px;top:1294px">Product Name 1</h3>
  <p class="abs product-copy" style="left:163px;top:1336px">Lorem ipsum dolor sit amet, consectetuer adipiscing elit, sed diam nonummy nibh euismod tincidunt ut laoreet dolore magna aliquam erat volutpat. Ut wisi enim ad minim veniam, quis nostrud exerci tation ullamcorper suscipit lobortis nisl ut aliquip ex ea commodo consequat. Duis autem vel eum iriure dolor in hendrerit in vulputate velit esse molestie consequat, vel illum dolore eu feugiat nulla facilisis.</p>
  <div class="ph large" role="img" aria-label="Product one trailer photo" style="left:589px;top:1261px;width:451px;height:263px"><span>Image Here</span></div>

  <div class="ph large" role="img" aria-label="Product two trailer photo" style="left:162px;top:1562px;width:450px;height:263px"><span>Image Here</span></div>
  <h3 class="abs heading product-name" style="left:641px;top:1590px">Product Name 2</h3>
  <p class="abs product-copy" style="left:644px;top:1632px">Lorem ipsum dolor sit amet, consectetuer adipiscing elit, sed diam nonummy nibh euismod tincidunt ut laoreet dolore magna aliquam erat volutpat. Ut wisi enim ad minim veniam, quis nostrud exerci tation ullamcorper suscipit lobortis nisl ut aliquip ex ea commodo consequat. Duis autem vel eum iriure dolor in hendrerit in vulputate velit esse molestie consequat, vel illum dolore eu feugiat nulla facilisis.</p>

  <h3 class="abs heading product-name" style="left:162px;top:1894px">Product Name 3</h3>
  <p class="abs product-copy" style="left:165px;top:1935px">Lorem ipsum dolor sit amet, consectetuer adipiscing elit, sed diam nonummy nibh euismod tincidunt ut laoreet dolore magna aliquam erat volutpat. Ut wisi enim ad minim veniam, quis nostrud exerci tation ullamcorper suscipit lobortis nisl ut aliquip ex ea commodo consequat. Duis autem vel eum iriure dolor in hendrerit in vulputate velit esse molestie consequat, vel illum dolore eu feugiat nulla facilisis.</p>
  <div class="ph large" role="img" aria-label="Product three trailer photo" style="left:589px;top:1853px;width:450px;height:263px"><span>Image Here</span></div>

  <a class="cta" href="#" style="left:375px;top:2161px">
    <svg width="26" height="26" viewBox="0 0 24 24" fill="none" stroke="currentColor" stroke-width="1.4"><path d="M5 3l4 1 1 5-2.5 1.5a12 12 0 0 0 6 6L15 14l5 1 1 4-2 2C10 21 3 14 3 5z"/><path d="M14 3a7 7 0 0 1 7 7M14 6a4 4 0 0 1 4 4"/></svg>
    Contact Us Today 555.018.2247
  </a>
  <a class="quote-btn" href="#" style="left:708px;top:2161px">Get Quote</a>
</section>

<footer>
  <div class="abs footer"></div>
  <div class="abs footer-brand"><span class="brand-dot"></span>Velvet Basin Suites</div>

  <div class="abs contact-box" style="left:546px;top:2363px">
    <svg width="22" height="22" viewBox="0 0 24 24" fill="none" stroke="#fff" stroke-width="1.3"><path d="M5 3l4 1 1 5-2.5 1.5a12 12 0 0 0 6 6L15 14l5 1 1 4-2 2C10 21 3 14 3 5z"/><path d="M14 3a7 7 0 0 1 7 7M14 6a4 4 0 0 1 4 4"/></svg>
  </div>
  <div class="abs contact-label" style="left:601px;top:2365px">Phone</div>
  <div class="abs contact-value" style="left:603px;top:2389px">07 5812 6640</div>

  <div class="abs contact-box" style="left:811px;top:2363px">
    <svg width="22" height="22" viewBox="0 0 24 24" fill="none" stroke="#fff" stroke-width="1.3"><path d="M3 10l9-6 9 6v10H3z"/><path d="M3 10l9 6 9-6"/><path d="M7 8h10M7 11h10"/></svg>
  </div>
  <div class="abs contact-label" style="left:868px;top:2363px">Email</div>
  <div class="abs contact-value" style="left:871px;top:2387px">sales@velvetbasin.com.au</div>

  <div class="abs rule"></div>
  <div class="abs copyright">© 2022&nbsp; Velvet Basin Suites. All Rights Reserved.</div>
</footer>

</body>
</html>
```